Telmoro Business Card

I already have the conplay logo. I need to develop a professional business card layout

Target Market(s)

Business

Industry/Entity Type

Business

Contact Information for Business Card

Company Name: Telmoro Limited

Font styles to use
Sans Serif

Colors

Designer to choose colors to be used in the design.

Requirements
Must have
• Use current logo
• Need two card size options:
• Small Card: 70mm x 28mm (Landscape)
• Square Card: 65mm x 65mm
Nice to have
• I will need 8-10 files for each name, number and email address (details to follow)

```html
<!DOCTYPE html>
<html lang="en">
<head>
<meta charset="utf-8">
<title>Telmoro Business Card</title>
<link href="https://fonts.googleapis.com/css2?family=Lato:wght@400;700&display=swap" rel="stylesheet">
<style>
  :root {
    --band-top: #1e7ac4;
    --band-bottom: #1467b5;
    --divider: #1e7ac4;
    --name: #4b4c9a;
    --title: #e8392f;
    --body: #222222;
    --brand: #1e7ac4;
    --paper: #ffffff;
  }
  html, body {
    margin: 0;
    padding: 0;
    width: 1200px;
    height: 1200px;
    overflow: hidden;
    background: var(--paper);
    font-family: "Lato", sans-serif;
  }
  .card {
    position: relative;
    width: 1200px;
    height: 1200px;
    background: var(--paper);
  }
  .band {
    position: absolute;
    left: 0;
    width: 1200px;
    height: 73px;
  }
  .band--top { top: 0; background: var(--band-top); }
  .band--bottom { bottom: 0; background: var(--band-bottom); }
  .brand-name {
    position: absolute;
    left: 61px;
    top: 548px;
    font-weight: 700;
    font-size: 118px;
    line-height: 1;
    color: var(--brand);
    letter-spacing: 1px;
  }
  .divider {
    position: absolute;
    left: 598px;
    top: 367px;
    width: 5px;
    height: 500px;
    background: var(--divider);
  }
  .details {
    position: absolute;
    left: 667px;
    top: 0;
  }
  .line {
    position: absolute;
    left: 0;
    white-space: nowrap;
    line-height: 1;
  }
  .person-name { top: 402px; font-size: 72px; color: var(--name); }
  .person-title { top: 478px; font-size: 43px; color: var(--title); }
  .address { font-size: 42px; color: var(--body); }
  .address--1 { top: 586px; }
  .address--2 { top: 637px; }
  .contact { font-size: 42px; color: var(--body); display: flex; align-items: center; }
  .contact--phone { top: 742px; }
  .contact--email { top: 803px; }
  .contact svg { width: 34px; height: 34px; margin-right: 20px; flex: none; }
</style>
</head>
<body>
  <main class="card">
    <div class="band band--top"></div>

    <div class="brand-name">Telmoro</div>

    <div class="divider"></div>

    <section class="details">
      <div class="line person-name">Marcus Ellery</div>
      <div class="line person-title">President</div>
      <div class="line address address--1">18 Harwick Lane,</div>
      <div class="line address address--2">Brookvale NSW 2100</div>
      <div class="line contact contact--phone">
        <svg viewBox="0 0 24 24" aria-hidden="true">
          <path fill="#1e7ac4" d="M6.6 10.8c1.4 2.8 3.8 5.1 6.6 6.6l2.2-2.2c.3-.3.7-.4 1-.2 1.1.4 2.3.6 3.6.6.6 0 1 .4 1 1V20c0 .6-.4 1-1 1C10.6 21 3 13.4 3 4c0-.6.4-1 1-1h3.5c.6 0 1 .4 1 1 0 1.3.2 2.5.6 3.6.1.3 0 .7-.2 1l-2.3 2.2z"/>
          <path fill="none" stroke="#1e7ac4" stroke-width="1.6" stroke-linecap="round" d="M14 3.5a7 7 0 0 1 6.5 6.5M14 7a3.5 3.5 0 0 1 3 3"/>
        </svg>
        +1 (555) 302 8847
      </div>
      <div class="line contact contact--email">
        <svg viewBox="0 0 24 24" aria-hidden="true">
          <rect x="2" y="5" width="20" height="14" fill="#1e7ac4"/>
          <path fill="none" stroke="#ffffff" stroke-width="1.5" d="M2.5 5.5 12 13l9.5-7.5M2.5 18.5l7-6M21.5 18.5l-7-6"/>
        </svg>
        info@telmoro.com
      </div>
    </section>

    <div class="band band--bottom"></div>
  </main>
</body>
</html>
```